Buchcover für ein Glücksbuch
Zielgruppe
Ich brauche ein Cover für mein Glücksbuch, es soll möglichst viele interessierte Leser ansprechen und zum Kauf des Buches animieren.
Mein Glücksbuch ist für jeden gedacht, der auch im Alltag in kleinen Dingen sein Glück sucht, es muss nicht immer das große Glück sein und auch Geld allein macht nicht glücklich. Es soll den Leser dazu bringen, das Glück in sich selbt zu finden. Es enthält Anleitungen und Tipps und eine Bonus-Mediation.
Aufgabenstellung
Der Titel des Buches lautet: 'Pfade zur Freude mit 12 Herzensfunken'
Untertitel: 'Heiter und gelassen jeden Tag mit Ideen und Übungen'
'Mit Bonus-Meditation'
Autorin (Pseudonym): Britta Wolder

```html
<!DOCTYPE html>
<html lang="de">
<head>
<meta charset="utf-8">
<title>Pfade zur Freude mit 12 Herzensfunken – Buchcover</title>
<link rel="stylesheet" href="https://fonts.googleapis.com/css2?family=Source+Sans+3:wght@400;500&family=Grandstander:wght@600&display=swap">
<style>
  :root {
    --backdrop: #e4e8e8;
    --cover-teal: #1aa8b6;
    --sun-yellow: #f7d335;
    --ink: #111414;
    --paper-white: #ffffff;
    --glow-pale: #eef8f8;
  }
  * { margin: 0; padding: 0; box-sizing: border-box; }
  html, body {
    width: 1200px;
    height: 1200px;
    overflow: hidden;
    background: var(--backdrop);
  }
  .canvas {
    position: relative;
    width: 1200px;
    height: 1200px;
  }
  .book-cover {
    position: absolute;
    left: 290px;
    top: 101px;
    width: 620px;
    height: 997px;
    background: var(--cover-teal);
    overflow: hidden;
    font-family: "Source Sans 3", "Myriad Pro", sans-serif;
    color: var(--ink);
  }
  .title {
    position: absolute;
    right: 84px;
    top: 40px;
    text-align: right;
    font-weight: 400;
  }
  .title-line {
    display: block;
    font-size: 37px;
    line-height: 1;
    white-space: nowrap;
  }
  .title-line--first { margin-bottom: 4px; }
  .title-highlight {
    font-family: "Grandstander", "Comic Sans MS", cursive;
    font-weight: 600;
    font-size: 80px;
    color: var(--sun-yellow);
    letter-spacing: 1px;
    vertical-align: -4px;
    margin-left: 6px;
  }
  .subtitle {
    position: absolute;
    left: 280px;
    width: 272px;
    top: 210px;
    text-align: center;
    color: var(--paper-white);
    font-size: 18px;
    line-height: 31px;
  }
  .illustration {
    position: absolute;
    left: 4px;
    top: 325px;
    width: 420px;
    height: 672px;
    border-radius: 210px 210px 0 0;
    background: radial-gradient(circle at 58% 34%, var(--glow-pale) 0%, rgba(238,248,248,0.85) 26%, rgba(247,211,53,0.35) 45%, rgba(26,168,182,0) 70%);
  }
  .bonus-note {
    position: absolute;
    left: 264px;
    width: 332px;
    top: 812px;
    text-align: center;
    color: var(--paper-white);
    font-size: 19px;
  }
  .author {
    position: absolute;
    right: 86px;
    top: 882px;
    font-size: 60px;
    font-weight: 400;
    line-height: 1;
    white-space: nowrap;
  }
</style>
</head>
<body>
<main class="canvas">
  <section class="book-cover">
    <h1 class="title">
      <span class="title-line title-line--first">Pfade zur<span class="title-highlight">Freude</span></span>
      <span class="title-line">mit 12 Herzensfunken</span>
    </h1>
    <p class="subtitle">Heiter und gelassen<br>jeden Tag<br>mit Ideen und Übungen</p>
    <div class="illustration" role="img" aria-label="Illustration: eine lächelnde Pusteblume mit weißem Kopf und gelbem Stiel, umgeben von gelben Funkelsternen"></div>
    <p class="bonus-note">Mit Bonus-Meditation</p>
    <p class="author">Britta Wolder</p>
  </section>
</main>
</body>
</html>
```